Billboard design 8x3M NURA (Spanish company)

We´re located in the south of Spain. We run a local telecom company.
We sell Fiber optic, and mobile phone lines mainly.
The billboard will have to be in Spanish, I would like the price to be something you spot on first sight when passing by in the car.
Our company color is blue, like in our logo which I will add. I will also add a example from what we currently have.
The new offer should be:
1000 megas + 100Gigas movil con llamadas ilimitadas. (meaning 1000Mb fiber optic speed and 100Gb data and unlimited calls for 1 mobile line)
Our details are: phone line 952 00 0147
Website: nu-ra.es

```html
<!DOCTYPE html>
<html lang="es">
<head>
<meta charset="utf-8">
<title>NURA – Valla 8x3</title>
<link rel="stylesheet" href="https://fonts.googleapis.com/css2?family=Poppins:wght@600;700;800&display=swap">
<style>
  :root {
    --blue-deep: #0b5a8c;
    --blue-mid: #137ab8;
    --blue-bright: #2aa8e3;
    --blue-band: #35ade6;
    --gold: #e1a92f;
    --white: #ffffff;
    --orange: #f38a17;
    --orange-light: #ffb23e;
    --page: #eef2f5;
  }
  * { margin: 0; padding: 0; box-sizing: border-box; }
  html, body {
    width: 1200px; height: 1125px; overflow: hidden;
    background: var(--page);
    font-family: "Poppins", Arial, sans-serif;
  }
  .billboard {
    position: absolute; left: 0; top: 337px;
    width: 1200px; height: 451px; overflow: hidden;
    background: linear-gradient(90deg, var(--blue-deep) 0%, var(--blue-mid) 30%, var(--blue-bright) 62%, var(--blue-bright) 100%);
    color: var(--white);
  }
  .billboard__curves { position: absolute; left: 0; top: 0; width: 420px; height: 415px; }
  .billboard__band {
    position: absolute; left: 0; bottom: 0; width: 100%; height: 36px;
    background: var(--blue-band);
  }
  .brand { position: absolute; left: 40px; top: 48px; }
  .brand__name { font-weight: 800; font-size: 58px; line-height: 1; letter-spacing: 4px; }
  .brand__services { font-weight: 600; font-size: 19px; margin-top: 14px; letter-spacing: 0.2px; }
  .tagline {
    position: absolute; left: 36px; top: 176px;
    font-weight: 700; font-size: 30px; line-height: 40px; letter-spacing: 0.3px;
  }
  .tagline__bar {
    position: absolute; left: 36px; top: 272px; width: 297px; height: 18px;
    background: var(--gold); border-radius: 9px;
  }
  .contact { position: absolute; left: 38px; color: var(--gold); font-weight: 700; white-space: nowrap; }
  .contact--phone { top: 302px; font-size: 37px; display: flex; align-items: center; gap: 14px; }
  .contact--web { top: 346px; font-size: 40px; }
  .offer__speed {
    position: absolute; left: 356px; top: 20px; width: 375px; height: 98px;
    background: var(--gold); border-radius: 20px;
    display: flex; align-items: baseline; justify-content: center; gap: 14px;
    padding-top: 2px; font-weight: 800;
  }
  .offer__speed-value { font-size: 90px; line-height: 98px; letter-spacing: -1px; }
  .offer__speed-unit { font-size: 46px; }
  .offer__data {
    position: absolute; left: 386px; top: 122px;
    font-weight: 700; font-size: 74px; line-height: 1;
  }
  .offer__mobile {
    position: absolute; left: 364px; top: 204px;
    font-weight: 700; font-size: 70px; line-height: 1;
    display: flex; align-items: center; gap: 16px;
  }
  .offer__calls {
    position: absolute; left: 367px; top: 276px;
    font-weight: 700; font-size: 37px; line-height: 1;
  }
  .offer__price {
    position: absolute; left: 392px; top: 330px;
    display: flex; align-items: baseline; gap: 10px; font-weight: 700;
  }
  .offer__price-label { font-size: 22px; }
  .offer__price-value { font-size: 80px; line-height: 1; letter-spacing: -1px; }
  .conditions {
    position: absolute; left: 972px; top: 32px;
    font-weight: 700; font-size: 14px;
  }
  .hero-art {
    position: absolute; left: 752px; top: 44px; width: 424px; height: 378px;
    border-radius: 40% 20% 8px 30%;
    background: radial-gradient(ellipse at 55% 60%, var(--orange-light) 0%, var(--orange) 55%, rgba(243,138,23,0) 75%);
  }
</style>
</head>
<body>
  <main class="billboard">
    <svg class="billboard__curves" viewBox="0 0 420 415" aria-hidden="true">
      <path d="M0 40 Q160 140 250 300 T420 415" fill="none" stroke="rgba(255,255,255,0.06)" stroke-width="60"/>
      <path d="M120 0 Q260 90 330 230" fill="none" stroke="rgba(255,255,255,0.05)" stroke-width="70"/>
    </svg>

    <div class="brand">
      <div class="brand__name">NURA</div>
      <div class="brand__services">Wifi | Fibra | Movil | Tv</div>
    </div>

    <h1 class="tagline">TU FIBRA + MÓVIL<br>AL MEJOR PRECIO</h1>
    <div class="tagline__bar"></div>

    <div class="contact contact--phone">
      <svg width="18" height="34" viewBox="0 0 18 34" aria-hidden="true">
        <rect x="1.5" y="1.5" width="15" height="31" rx="3" fill="none" stroke="#ffffff" stroke-width="2.2"/>
        <circle cx="9" cy="28" r="1.5" fill="#ffffff"/>
      </svg>
      <span>952 00 0147</span>
    </div>
    <div class="contact contact--web">www.nu-ra.es</div>

    <div class="offer__speed">
      <span class="offer__speed-value">1000</span><span class="offer__speed-unit">Mb</span>
    </div>
    <div class="offer__data">+ 100 Gb</div>
    <div class="offer__mobile">
      <svg width="30" height="56" viewBox="0 0 30 56" aria-hidden="true">
        <rect x="2" y="2" width="26" height="52" rx="5" fill="none" stroke="#ffffff" stroke-width="3"/>
        <circle cx="15" cy="46" r="2.4" fill="#ffffff"/>
      </svg>
      <span>móvil con</span>
    </div>
    <div class="offer__calls">llamadas ilimitadas</div>
    <div class="offer__price">
      <span class="offer__price-label">por</span>
      <span class="offer__price-value">18.45€</span>
    </div>

    <div class="conditions">*Consulte condiciones</div>

    <div class="hero-art" role="img" aria-label="Ilustración de un cohete despegando desde un portátil entre nubes de humo naranja"></div>

    <div class="billboard__band"></div>
  </main>
</body>
</html>
```